Before & After School Care Business - Service Promotional Flyer

Need service promotional flyer for when parents (customers) are enrolling kids in school for first time. This flyer is specifically aimed at parents with kids aged 4 - 7 years old and needs to communicate crazy, fun and energy. We have five programs which we operate every school daily all based within local school halls. The flyer will be added to the local schools welcome to school pack. We also run School Holiday Programs supporting busy working families.

```html
<!DOCTYPE html>
<html lang="en">
<head>
<meta charset="utf-8">
<title>Play Patch – Out of School Care Flyer</title>
<link href="https://fonts.googleapis.com/css2?family=Roboto+Condensed:wght@400;700&family=Lato:wght@400;700&display=swap" rel="stylesheet">
<style>
  :root {
    --magenta: #e5177e;
    --cyan: #1aa7e3;
    --yellow: #f6eb14;
    --white: #ffffff;
    --ink: #1d1d1b;
    --paper: #ffffff;
  }
  * { box-sizing: border-box; margin: 0; padding: 0; }
  html, body { width: 902px; height: 1200px; overflow: hidden; background: var(--paper); }
  .flyer {
    position: relative; width: 902px; height: 1200px; overflow: hidden;
    background: var(--paper);
    font-family: "Roboto Condensed", Arial, sans-serif;
  }
  .hero-photo {
    position: absolute; left: 40px; top: 150px; width: 840px; height: 500px;
    background: radial-gradient(ellipse at 50% 60%, #f4d9c4 0%, #e9c8ae 35%, #f7f3ee 75%, #ffffff 100%);
  }
  .bands { position: absolute; left: 0; top: 0; width: 902px; height: 1200px; }
  .programs-backdrop {
    position: absolute; left: 362px; top: 772px; width: 540px; height: 364px;
    background: linear-gradient(135deg, #f6f6f6, #ebebeb 60%, #f7f7f7);
  }
  .brand {
    position: absolute; top: 70px; left: 0; width: 902px; height: 46px;
    display: flex; justify-content: center; align-items: center; gap: 12px;
  }
  .brand-dot { width: 34px; height: 34px; border-radius: 50%; background: var(--cyan); }
  .brand-name { font-weight: 700; font-size: 40px; line-height: 1; color: var(--cyan); letter-spacing: 1px; }
  .photo-badge {
    position: absolute; border-radius: 50%;
    border: 10px solid var(--yellow); box-shadow: 0 0 0 6px var(--white) inset;
  }
  .badge-faces {
    left: 92px; top: 487px; width: 280px; height: 280px;
    background: radial-gradient(circle at 50% 50%, #f2cdb3, #e8b894 55%, #ffffff 100%);
  }
  .badge-reading {
    left: 37px; top: 641px; width: 230px; height: 230px;
    background: radial-gradient(circle at 50% 55%, #d9c2a4, #b7c9e0 55%, #ffffff 100%);
  }
  .headline {
    position: absolute; left: 380px; top: 592px; width: 500px; text-align: center;
    white-space: nowrap;
  }
  .headline-name {
    font-weight: 700; font-size: 88px; line-height: 92px; color: var(--magenta);
    text-shadow: 3px 3px 0 var(--white);
  }
  .headline-tag {
    font-weight: 700; font-size: 48px; line-height: 50px; color: var(--cyan);
    text-shadow: 2px 2px 0 var(--white);
  }
  .reserve {
    position: absolute; left: 33px; top: 898px; width: 320px;
    font-weight: 700; font-size: 28px; line-height: 39px; color: var(--cyan);
    white-space: nowrap;
  }
  .programs { position: absolute; left: 387px; top: 800px; }
  .programs-title { font-size: 28px; line-height: 36px; color: var(--cyan); margin-bottom: 12px; }
  .program-list { list-style: none; font-family: "Lato", Arial, sans-serif; font-size: 21px; color: var(--ink); }
  .program-list li { display: flex; align-items: center; height: 40px; margin-left: 30px; white-space: nowrap; }
  .program-num {
    width: 22px; height: 22px; border-radius: 50% 50% 50% 0; background: var(--magenta);
    color: var(--white); font-size: 13px; font-weight: 700;
    display: flex; align-items: center; justify-content: center; margin-right: 12px;
  }
  .call-out {
    position: absolute; left: 440px; top: 1068px; width: 440px; text-align: right;
    font-size: 42px; line-height: 50px; color: var(--magenta); white-space: nowrap;
  }
  .contacts { position: absolute; left: 38px; top: 1062px; list-style: none;
    font-family: "Lato", Arial, sans-serif; font-size: 21px; color: var(--ink); }
  .contacts li { display: flex; align-items: center; height: 34px; white-space: nowrap; }
  .contacts svg { width: 20px; height: 20px; margin-right: 12px; }
</style>
</head>
<body>
<main class="flyer">
  <div class="hero-photo" role="img" aria-label="Photo of five happy school children with backpacks raising their arms"></div>
  <div class="programs-backdrop" role="img" aria-label="Faint background of alphabet toy blocks"></div>

  <svg class="bands" viewBox="0 0 902 1200" aria-hidden="true">
    <path d="M0,560 C300,610 650,560 902,420 L902,620 C620,700 320,760 0,880 Z" fill="var(--magenta)"/>
    <path d="M0,520 C300,590 650,560 902,465 L902,744 C640,754 420,762 0,792 Z" fill="var(--cyan)"/>
    <path d="M0,545 C300,615 650,590 902,500 L902,730 C640,740 420,747 0,777 Z" fill="var(--yellow)"/>
    <path d="M0,1030 L330,1030 C380,1030 395,1080 412,1136 L902,1136 L902,1200 L0,1200 Z" fill="var(--yellow)"/>
    <rect x="0" y="1170" width="902" height="30" fill="var(--cyan)"/>
  </svg>

  <header class="brand">
    <span class="brand-dot"></span>
    <span class="brand-name">PLAY PATCH</span>
  </header>

  <div class="photo-badge badge-faces" role="img" aria-label="Photo of three smiling children with painted faces"></div>
  <div class="photo-badge badge-reading" role="img" aria-label="Illustration of a girl reading on a stack of books with learning symbols"></div>

  <section class="headline">
    <h1 class="headline-name">PLAY PATCH</h1>
    <p class="headline-tag">LETTING KIDS BE KIDS</p>
  </section>

  <p class="reserve">Reserve your place in<br>one of our Before,<br>After School or School<br>Holiday Programmes.</p>

  <section class="programs">
    <h2 class="programs-title">Our Programs:</h2>
    <ol class="program-list">
      <li><span class="program-num">1</span>Lorem ipsum dolor sit amet,</li>
      <li><span class="program-num">2</span>consectetuer adipiscing elit.</li>
      <li><span class="program-num">3</span>Aenean commodo ligula eget dolor.</li>
      <li><span class="program-num">4</span>Aenean massa.</li>
      <li><span class="program-num">5</span>Cum sociis natoque penatibus et</li>
    </ol>
  </section>

  <p class="call-out">"Hurry! Give us a call..."</p>

  <ul class="contacts">
    <li><svg viewBox="0 0 20 20"><rect x="5" y="1" width="10" height="18" rx="2" fill="var(--magenta)"/><rect x="7" y="4" width="6" height="8" fill="var(--yellow)"/></svg>0800 555 0123</li>
    <li><svg viewBox="0 0 20 20"><rect x="1" y="4" width="18" height="12" fill="var(--magenta)"/><path d="M1,4 L10,11 L19,4" stroke="var(--yellow)" stroke-width="1.5" fill="none"/></svg>hello@playpatch.co.nz</li>
    <li><svg viewBox="0 0 20 20"><circle cx="10" cy="10" r="9" fill="var(--magenta)"/><path d="M1,10 H19 M10,1 C5,6 5,14 10,19 M10,1 C15,6 15,14 10,19" stroke="var(--yellow)" stroke-width="1.2" fill="none"/></svg>playpatch.co.nz</li>
  </ul>
</main>
</body>
</html>
```